A suite of 3-4 brand templates.

I would like various brand templates using my brand colours(see my logo) that I can add information to, so I can create different help guides/ infographics on various health and well being topics (anxiety, breathing techniques, pain relief, self hypnosis etc) that I can put on my website:-
www.brightlanewellness.com

I want to ability to add both text guides and other guides to be more visual.

Target Market(s)

Health and wellbeing clients (particularly people looking for hypnosis, pain reprocessing therapy, and health coaching.

Industry/Entity Type

Health and Psychology

Font styles to use
Sans Serif

Colors
0054AA
0677BA
7BADD7
CADEEF
E8F1F8
0094D4
00A9DD
6FCCEA
C7EBF8
E9F6FB
F0912C
F2A743
F7CA91
FBE8D2
FDF5EE

Requirements
Must have
• Brand colours, website and Logo
Nice to have
• To look visually appealing and professional.

```html
<!DOCTYPE html>
<html lang="en">
<head>
<meta charset="utf-8">
<title>Bright Lane Wellness – Guide Template</title>
<link href="https://fonts.googleapis.com/css2?family=Poppins:wght@400;500;600;700;800&family=Roboto:wght@700&display=swap" rel="stylesheet">
<style>
  :root{
    --navy:#1f4f8b;
    --title-orange:#f26b0f;
    --icon-orange:#f2a743;
    --dot-orange:#f7943a;
    --bar-orange:#fb9a35;
    --ink:#1c1c1c;
    --wire-grey:#8a8a8a;
    --wire-rule:#c9c9c9;
    --white:#ffffff;
    --stage-light:#d9d6d6;
    --stage-dark:#838383;
  }
  *{margin:0;padding:0;box-sizing:border-box;}
  html,body{width:1065px;height:1200px;overflow:hidden;}
  body{font-family:"Poppins",sans-serif;color:var(--ink);}
  .board{
    position:relative;width:1065px;height:1200px;overflow:hidden;
    background:radial-gradient(ellipse at 50% 52%,var(--stage-light) 0%,#b4b2b2 30%,var(--stage-dark) 70%);
  }
  .abs{position:absolute;}

  /* ---------- full guide page ---------- */
  .guide{left:57px;top:88px;width:951px;height:535px;background:var(--white);}
  .nav{left:0;top:0;width:951px;height:39px;background:var(--navy);}
  .nav span{position:absolute;top:13px;font:800 7.6px/13px "Poppins",sans-serif;color:var(--white);letter-spacing:-0.1px;white-space:nowrap;}
  .nav .caret{display:inline-block;width:4px;height:4px;border-right:1.2px solid #fff;border-bottom:1.2px solid #fff;transform:rotate(45deg);margin-left:3px;position:relative;top:-2px;}

  .brand{display:flex;flex-direction:column;align-items:center;}
  .brand-mark{border-radius:50%;background:var(--icon-orange);}
  .brand-name{font-family:"Poppins",sans-serif;font-weight:600;color:var(--navy);white-space:nowrap;}

  .guide-title{left:104px;top:187px;width:300px;text-align:right;
    font:700 25px/27px "Roboto",sans-serif;letter-spacing:-0.2px;white-space:nowrap;}
  .guide-title .line-a{color:var(--navy);display:block;}
  .guide-title .line-b{color:var(--title-orange);display:block;}
  .guide-intro{left:180px;top:263px;width:224px;text-align:right;font:400 10.3px/14.6px "Poppins",sans-serif;}

  .section-head{font:600 21px/26px "Poppins",sans-serif;color:var(--navy);white-space:nowrap;}
  .steps{list-style:none;width:230px;}
  .steps li{position:relative;padding-left:25px;font:400 10.3px/14.5px "Poppins",sans-serif;margin-bottom:7.5px;}
  .steps li::before{content:"";position:absolute;left:3px;top:2px;width:11px;height:11px;border-radius:50%;background:var(--dot-orange);}
  .evidence-text{width:240px;font:400 10.3px/14.6px "Poppins",sans-serif;}

  /* ---------- wireframe ---------- */
  .wire{left:158px;top:690px;width:749px;height:421px;background:var(--white);border:1px solid var(--wire-rule);}
  .wire-band{left:0;top:0;width:747px;height:30px;background:var(--navy);}
  .wire-rule{top:30px;width:1px;height:389px;background:var(--wire-rule);}
  .wire-bar{height:13.5px;}
  .wire-line{height:5px;background:var(--wire-grey);}
  .wire-dot{width:9px;height:9px;border-radius:50%;background:var(--dot-orange);}
  .wire-block-navy{background:var(--navy);}
  .wire-block-orange{background:var(--bar-orange);}
</style>
</head>
<body>
<svg width="0" height="0" style="position:absolute">
  <defs>
    <symbol id="icon-question" viewBox="0 0 48 46">
      <rect x="16" y="0" width="32" height="33" rx="6" fill="#f2a743"/>
      <path d="M10 6h24a8 8 0 0 1 8 8v13a8 8 0 0 1-8 8h-6l-6 8-6-8h-6a8 8 0 0 1-8-8V14a8 8 0 0 1 8-8z" fill="none" stroke="#1f4f8b" stroke-width="2.8" stroke-linejoin="round"/>
      <path d="M16.5 16.5a5.5 5.5 0 1 1 7.5 5.1c-1.6.7-2 1.6-2 3.4" fill="none" stroke="#1f4f8b" stroke-width="2.8" stroke-linecap="round"/>
      <circle cx="22" cy="30" r="1.8" fill="#1f4f8b"/>
    </symbol>
    <symbol id="icon-evidence" viewBox="0 0 48 50">
      <rect x="16" y="0" width="32" height="32" rx="6" fill="#f2a743"/>
      <path d="M4 7h20l7 7v7M31 37v7a2 2 0 0 1-2 2H4a2 2 0 0 1-2-2V9a2 2 0 0 1 2-2" fill="#fff" stroke="#1f4f8b" stroke-width="2.4" stroke-linejoin="round"/>
      <path d="M24 7v7h7" fill="none" stroke="#1f4f8b" stroke-width="2.4" stroke-linejoin="round"/>
      <path d="M7 14h12M7 19h15M7 24h12M7 29h10M7 34h12M7 39h15" stroke="#1f4f8b" stroke-width="2.4" stroke-linecap="round"/>
      <circle cx="31" cy="29" r="7.5" fill="#f2a743" stroke="#1f4f8b" stroke-width="2.4"/>
      <path d="M27.5 29l2.5 2.5 4.5-4.5" fill="none" stroke="#1f4f8b" stroke-width="2.2" stroke-linecap="round" stroke-linejoin="round"/>
      <path d="M36 35l6 8" stroke="#1f4f8b" stroke-width="3.6" stroke-linecap="round"/>
    </symbol>
  </defs>
</svg>

<div class="board">

  <section class="guide abs">
    <nav class="nav abs">
      <span style="left:314px">HOME</span>
      <span style="left:360px">THERAPIES<i class="caret"></i></span>
      <span style="left:432px">MY APPROACH</span>
      <span style="left:514px">RESOURCES</span>
      <span style="left:583px">CONTACT ME</span>
    </nav>

    <div class="brand abs" style="left:138px;top:76px;width:82px;">
      <div class="brand-mark" style="width:44px;height:44px;"></div>
      <div class="brand-name" style="font-size:8.6px;margin-top:7px;">BRIGHT LANE WELLNESS</div>
    </div>

    <h1 class="guide-title abs">
      <span class="line-a">Resonance (Coherent)</span>
      <span class="line-b">Breathing Mechanism</span>
    </h1>
    <p class="guide-intro abs">Activates the parasympathetic nervous system by synchronizing heart rate variability (HRV) and respiration, creating a state of physiological coherence.</p>

    <svg class="abs" style="left:529px;top:190px" width="49" height="47" aria-hidden="true"><use href="#icon-question"/></svg>
    <h2 class="section-head abs" style="left:593px;top:186px;">How to do it:</h2>
    <ul class="steps abs" style="left:596px;top:218px;">
      <li>Inhale gently through the nose for 5.5–6 seconds</li>
      <li>Exhale gently through the mouth for 5.5–6 seconds</li>
      <li>Continue for 5 minutes, focusing on smooth rhythm and comfort</li>
    </ul>

    <svg class="abs" style="left:529px;top:355px" width="47" height="50" aria-hidden="true"><use href="#icon-evidence"/></svg>
    <h2 class="section-head abs" style="left:593px;top:350px;">Evidence:</h2>
    <p class="evidence-text abs" style="left:593px;top:380px;">Studies show resonance breathing (around 0.1 Hz or 6 breaths per minute) enhances HRV, reduces blood pressure, and improves emotional regulation. Hallam et al., 2020, Northfield Psychology Review Moretti et al., 2018, Northfield Human Neuroscience</p>
  </section>

  <section class="wire abs" aria-label="Layout grid">
    <div class="wire-band abs"></div>
    <div class="wire-rule abs" style="left:104px"></div>
    <div class="wire-rule abs" style="left:322px"></div>
    <div class="wire-rule abs" style="left:426px"></div>
    <div class="wire-rule abs" style="left:644px"></div>

    <div class="brand abs" style="left:109px;top:59px;width:66px;">
      <div class="brand-mark" style="width:36px;height:36px;"></div>
      <div class="brand-name" style="font-size:6.6px;margin-top:5px;">BRIGHT LANE WELLNESS</div>
    </div>

    <div class="wire-bar wire-block-navy abs" style="left:105px;top:151px;width:210px;"></div>
    <div class="wire-bar wire-block-orange abs" style="left:105px;top:174px;width:210px;"></div>
    <div class="wire-line abs" style="left:155px;top:212px;width:162px;"></div>
    <div class="wire-line abs" style="left:155px;top:224px;width:162px;"></div>
    <div class="wire-line abs" style="left:155px;top:236px;width:162px;"></div>
    <div class="wire-line abs" style="left:155px;top:248px;width:162px;"></div>

    <svg class="abs" style="left:427px;top:149px" width="38" height="37" aria-hidden="true"><use href="#icon-question"/></svg>
    <div class="wire-bar wire-block-navy abs" style="left:476px;top:151px;width:102px;"></div>
    <div class="wire-dot abs" style="left:480px;top:172px;"></div>
    <div class="wire-line abs" style="left:496px;top:174px;width:145px;"></div>
    <div class="wire-line abs" style="left:496px;top:186px;width:67px;"></div>
    <div class="wire-dot abs" style="left:480px;top:201px;"></div>
    <div class="wire-line abs" style="left:496px;top:203px;width:145px;"></div>
    <div class="wire-line abs" style="left:496px;top:215px;width:67px;"></div>
    <div class="wire-dot abs" style="left:480px;top:231px;"></div>
    <div class="wire-line abs" style="left:496px;top:232px;width:145px;"></div>
    <div class="wire-line abs" style="left:496px;top:244px;width:67px;"></div>

    <svg class="abs" style="left:427px;top:279px" width="38" height="40" aria-hidden="true"><use href="#icon-evidence"/></svg>
    <div class="wire-bar wire-block-navy abs" style="left:476px;top:280px;width:102px;"></div>
    <div class="wire-line abs" style="left:477px;top:305px;width:162px;"></div>
    <div class="wire-line abs" style="left:477px;top:317px;width:162px;"></div>
    <div class="wire-line abs" style="left:477px;top:329px;width:162px;"></div>
    <div class="wire-line abs" style="left:477px;top:342px;width:162px;"></div>
    <div class="wire-line abs" style="left:477px;top:354px;width:75px;"></div>
  </section>

</div>
</body>
</html>
```